Business Card Design

I am a florist specialising in weddings. I would like a very modern however elegant and simple design. My arrangement designs can be quite rustic with a vintage feel, so if you are able to reflect this in the card that would be great.
Updates

Thank you everyone for your submissions. I have found some further words for inspiration. I am looking for something more earthy and artisan looking. If possible I would like to use 100% recycled paper - the type that even looks rustic and recycled. I may even opt to use a small logo to emphasis the fact that they are made from recycled paper. I know this is quite different to my original brief but I wasn't quite sure what to expect from your designs. Also, with the logo, I give permission for it to be cropped to remove the 'Floral Designer' text. Please contact me if you need any further assistance. Many thanks Lisette Petal and Thistle Studio

I would prefer not to have any photgraphs & not too much pink. Thank you!

Industry/Entity Type

Florist

Contact Information for Business Card

Lisette Varko
Floral Designer
0417 365 820
lisette@petalthistlestudio.com.au
petalthistlestudio.com.au

Requirements
Must have
• My logo

```html
<!DOCTYPE html>
<html lang="en">
<head>
<meta charset="utf-8">
<title>Petal and Thistle Studio – Business Card</title>
<link rel="stylesheet" href="https://fonts.googleapis.com/css2?family=Lato:wght@400;700;900&display=swap">
<style>
  :root {
    --paper: #ffffff;
    --ink: #111111;
    --name-grey: #b5b5b5;
    --rose: #c8448d;
    --rule-dark: #3a3a3a;
  }
  * { margin: 0; padding: 0; box-sizing: border-box; }
  html, body {
    width: 1200px;
    height: 741px;
    overflow: hidden;
    background: var(--paper);
  }
  .card {
    position: relative;
    width: 1200px;
    height: 741px;
    background: var(--paper);
    font-family: "Lato", Arial, sans-serif;
    color: var(--ink);
  }
  .identity {
    position: absolute;
    left: 76px;
    top: 90px;
  }
  .identity__name {
    font-size: 35px;
    font-weight: 900;
    letter-spacing: 0.2px;
    color: var(--name-grey);
    text-transform: uppercase;
    line-height: 1.1;
  }
  .identity__role {
    margin-top: 2px;
    font-size: 28px;
    font-weight: 700;
    text-transform: uppercase;
    line-height: 1.1;
  }
  .brand {
    position: absolute;
    right: 62px;
    top: 150px;
    display: flex;
    align-items: center;
    gap: 14px;
  }
  .brand__dot {
    width: 22px;
    height: 22px;
    border-radius: 50%;
    background: var(--rose);
  }
  .brand__name {
    font-size: 42px;
    font-weight: 400;
    color: var(--ink);
    line-height: 1;
  }
  .services {
    position: absolute;
    left: 78px;
    top: 428px;
    display: flex;
    align-items: center;
    font-size: 26.5px;
    font-weight: 900;
    text-transform: uppercase;
  }
  .services__divider {
    width: 3px;
    height: 62px;
    margin: 0 6px;
    background: linear-gradient(to bottom, rgba(58,58,58,0), var(--rule-dark) 30%, var(--rule-dark) 70%, rgba(58,58,58,0));
  }
  .contact {
    position: absolute;
    left: 76px;
    display: flex;
    align-items: center;
    gap: 20px;
    font-size: 28px;
    font-weight: 700;
  }
  .contact svg { width: 32px; height: 26px; fill: var(--ink); }
  .contact--phone { top: 518px; }
  .contact--email { top: 573px; }
  .website {
    position: absolute;
    left: 78px;
    top: 637px;
    font-size: 33px;
    font-weight: 900;
  }
  .website__domain { color: var(--rose); }
</style>
</head>
<body>
  <div class="card">
    <header class="identity">
      <h1 class="identity__name">Lisette Varko</h1>
      <p class="identity__role">Floral Designer</p>
    </header>

    <div class="brand">
      <span class="brand__dot"></span>
      <span class="brand__name">Petal and Thistle Studio</span>
    </div>

    <div class="services">
      <span>Weddings</span>
      <span class="services__divider"></span>
      <span>Events</span>
      <span class="services__divider"></span>
      <span>Special Occasions</span>
    </div>

    <div class="contact contact--phone">
      <svg viewBox="0 0 32 26" aria-hidden="true">
        <path d="M2 9c0-4 6-7 14-7s14 3 14 7v3h-7V8c-2-1-4-1.5-7-1.5S11 7 9 8v4H2z"/>
        <path d="M8 13h16l4 11H4z"/>
      </svg>
      <span>0417 365 820</span>
    </div>

    <div class="contact contact--email">
      <svg viewBox="0 0 32 26" aria-hidden="true">
        <path d="M3 3h26v20H3z M6 6v1l10 8 10-8V6z M6 10v10h20V10l-10 8z" fill-rule="evenodd"/>
      </svg>
      <span>lisette@petalthistlestudio.com.au</span>
    </div>

    <div class="website">www.<span class="website__domain">petalthistlestudio</span>.com.au</div>
  </div>
</body>
</html>
```